Commercial Real Estate for Lease Listing Flyer

I am looking to put together a flyer for our available office space in our building. It needs to look professional and it will be standard sized 8.5 x 11 and double sided. Full color as well. This flyer will need to be able to be put in a PDF and a picture file that can be embedded in an email. I have included pictures, logo, and a Word document with the information you should need. Also, I included a bunch of SAMPLE leasing flyers that you can get ideas from. The floor plan is also included in here. I want it specifically noted that the top suite is Suite 100 and the bottom suite is 120. And list their size as well. I will be reviewing all designs very quickly, so be sure to check the comments.

Requirements
Must have
• Please refer to these links for additional photos:
• "Twilight 1.jpg" at: https://files.quorvane.net/a/preview/7e2d1f90-3b4c-4a8e-b1d2-5c6f7a8b9c01
• Twilight 2_straightened.jpg" at: https://files.quorvane.net/a/preview/4b8c2e71-9d0a-4f3b-a6c5-2e1d0f9a8b72
• "Twilight 3.jpg" at: https://files.quorvane.net/a/preview/5c9d3f82-0e1b-4a4c-b7d6-3f2e1a0b9c83
• "Twilight 4.jpg" at: https://files.quorvane.net/a/preview/6d0e4a93-1f2c-4b5d-88e7-4a3f2b1c0d94
• "Twilight 5.jpg" at: https://files.quorvane.net/a/preview/7e1f5ba4-2a3d-4c6e-99f8-5b4a3c2d1ea5
• "Twilight 6.jpg" at: https://files.quorvane.net/a/preview/8f2a6cb5-3b4e-4d7f-8a09-6c5b4d3e2fb6
• "Twilight 7.jpg" at: https://files.quorvane.net/a/preview/9a3b7dc6-4c5f-4e80-9b1a-7d6c5e4f3ac7
• "Twilight 8.jpg" at: https://files.quorvane.net/a/preview/1b4c8ed7-5d6a-4f91-8c2b-8e7d6f5a4bd8
• "Twilight 9.jpg" at: https://files.quorvane.net/a/preview/2c5d9fe8-6e7b-4a02-9d3c-9f8e7a6b5ce9
• "Twilight 10.jpg" at: https://files.quorvane.net/a/preview/3d6e0af9-7f8c-4b13-8e4d-0a9f8b7c6dfa
• "Twilight 11.jpg" at: https://files.quorvane.net/a/preview/4e7f1b0a-8a9d-4c24-9f5e-1b0a9c8d7e0b

```html
<!DOCTYPE html>
<html lang="en">
<head>
<meta charset="utf-8">
<title>Harbor Ridge Centre – Office Space for Lease</title>
<link rel="stylesheet" href="https://fonts.googleapis.com/css2?family=Montserrat:wght@300;400;500;600;700;800&display=swap">
<style>
  :root {
    --brand-blue: #0a599c;
    --text-gray: #5b5c5f;
    --heading-gray: #6b6c6f;
    --paper: #ffffff;
    --plan-tone: #eef0f3;
    --photo-warm-a: #b59468;
    --photo-warm-b: #4b3526;
    --photo-room-a: #c9ad84;
    --photo-room-b: #3d2e25;
  }
  * { box-sizing: border-box; margin: 0; padding: 0; }
  html, body { width: 946px; height: 1200px; overflow: hidden; background: var(--paper); }
  body { font-family: "Montserrat", sans-serif; color: var(--text-gray); }

  .flyer { position: relative; width: 946px; height: 1200px; background: var(--paper); }

  .band-top { position: absolute; left: 0; top: 0; width: 100%; height: 41px; background: var(--brand-blue); }
  .band-bottom { position: absolute; left: 0; bottom: 0; width: 100%; height: 38px; background: var(--brand-blue); }

  .features-title { position: absolute; left: 70px; top: 80px; line-height: 1.2; }
  .features-title .line-light { display: block; font-size: 38px; font-weight: 400; color: var(--brand-blue); letter-spacing: 0.5px; }
  .features-title .line-bold { display: block; font-size: 38px; font-weight: 800; color: var(--heading-gray); letter-spacing: 0.5px; }
  .features-rule { position: absolute; left: 70px; top: 176px; width: 292px; height: 3px; background: var(--brand-blue); }

  .amenity-list { position: absolute; left: 85px; top: 209px; list-style: none; }
  .amenity-list li { position: relative; padding-left: 37px; font-size: 21.5px; font-weight: 500; line-height: 24px; margin-bottom: 12px; color: var(--text-gray); letter-spacing: 0.3px; }
  .amenity-list li::before { content: ""; position: absolute; left: 0; top: 5px; width: 13px; height: 13px; background: var(--brand-blue); box-shadow: -2px 2px 0 #7b98b8; }

  .floor-plan { position: absolute; left: 463px; top: 57px; width: 427px; height: 336px; background: linear-gradient(135deg, #f6f7f9, var(--plan-tone)); border: 1px solid #d4d8de; }

  .rate-band { position: absolute; left: 0; top: 405px; width: 100%; height: 165px; background: var(--brand-blue); color: #fff; }
  .rate-band h2 { position: absolute; left: 71px; top: 30px; font-size: 25px; font-weight: 700; letter-spacing: 0.2px; }
  .rate-band p { position: absolute; left: 85px; font-size: 19px; font-weight: 500; letter-spacing: 0.2px; }
  .rate-band .note-1 { top: 77px; }
  .rate-band .note-2 { top: 113px; }

  .tab { position: absolute; left: 699px; width: 147px; background: var(--brand-blue); }
  .tab-1 { top: 570px; height: 38px; }
  .tab-2 { top: 847px; height: 35px; }
  .tab-3 { top: 1123px; height: 40px; }

  .photo { position: absolute; left: 653px; width: 241px; height: 220px; }
  .photo-office { top: 619px; background: linear-gradient(180deg, var(--photo-warm-a) 0%, #8d6c4b 55%, var(--photo-warm-b) 100%); }
  .photo-meeting { top: 893px; background: linear-gradient(180deg, var(--photo-room-a) 0%, #7d6048 55%, var(--photo-room-b) 100%); }

  .details { position: absolute; left: 75px; top: 592px; width: 540px; list-style: none; }
  .details > li { position: relative; padding-left: 21px; font-size: 14.6px; line-height: 25px; font-weight: 400; color: var(--text-gray); }
  .details > li::before { content: ""; position: absolute; left: 0; top: 8px; width: 10px; height: 10px; background: var(--brand-blue); box-shadow: -1px 1px 0 #7b98b8; }
  .details .d1 { margin-bottom: 19px; }
  .details .d2 { margin-bottom: 19px; }
  .details .d3 { margin-bottom: 19px; }

  .suite-list { list-style: none; margin-top: 9px; }
  .suite-list li { position: relative; padding-left: 29px; font-size: 14.6px; line-height: 22px; margin-bottom: 22px; }
  .suite-list li svg { position: absolute; left: 12px; top: 6px; }
</style>
</head>
<body>
<main class="flyer">
  <div class="band-top"></div>

  <h1 class="features-title">
    <span class="line-light">FEATURES &amp;</span>
    <span class="line-bold">AMENITIES</span>
  </h1>
  <div class="features-rule"></div>

  <ul class="amenity-list">
    <li>Plenty of parking</li>
    <li>On-site management</li>
    <li>Some furniture<br>available if needed.</li>
  </ul>

  <div class="floor-plan" role="img" aria-label="Floor plan of Suites 100 and 120 showing offices, conference room, break rooms and reception"></div>

  <section class="rate-band">
    <h2>Rental Rate: $32.00/SF plus suite electric</h2>
    <p class="note-1">- No extra operating expenses.</p>
    <p class="note-2">- Very easy to show as landlord is in the building.</p>
  </section>

  <div class="tab tab-1"></div>
  <div class="photo photo-office" role="img" aria-label="Photo of a furnished private office with a wood desk and executive chair"></div>
  <div class="tab tab-2"></div>
  <div class="photo photo-meeting" role="img" aria-label="Photo of a meeting room with a long conference table and arched window"></div>
  <div class="tab tab-3"></div>

  <ul class="details">
    <li class="d1">The Harbor Ridge Centre is a beautiful Class A building situation<br>in the heart of Coral Bay Gardens but without the<br>crazy Parkway traffic.</li>
    <li class="d2">Harbor Ridge Centre is located directly on the Bayline Expressway<br>just off of Harbor Ridge Road. The massive, new Westmere development<br>south entrance is being built across the street. The building is very<br>convenient to restaurants, shopping, and every other trade needed.</li>
    <li class="d3">The suites are incredibly well appointed and move-in ready with<br>custom oak doors and millwork, 10’ ceilings, floor to ceiling<br>windows</li>
    <li class="d4">Two suites are available, which can be combined for 3,791 SF in total.
      <ul class="suite-list">
        <li><svg width="7" height="10" viewBox="0 0 7 10"><path d="M1 1l4 4-4 4" fill="none" stroke="#0a599c" stroke-width="2"/></svg>Suite 120 is available right now and is 1,488 SF with 1<br>large executive office, 2 smaller offices, a conference room,<br>break room, and reception area.</li>
        <li><svg width="7" height="10" viewBox="0 0 7 10"><path d="M1 1l4 4-4 4" fill="none" stroke="#0a599c" stroke-width="2"/></svg>Suite 100 is available in February 2019, but could be<br>vacated sooner. Suite 120 is 2,303 SF and has 6 offices,<br>break room, reception area, and a very large meeting<br>room.</li>
      </ul>
    </li>
  </ul>

  <div class="band-bottom"></div>
</main>
</body>
</html>
```